brochure for high-end senior living company

We need a new brochure that we can pass out to doctors and social workers so they would choose us over the competition.
brightmeadowhaven.example is our website that shows our colors and themes

we stand out over our competition due to our high quality of staff and our staff to resident ratio.
We are not afraid of difficult and complex care situations. Instead, we thrive on coordinating complexity.

We do all of this in a lovely setting that is luxurious and feels like home.

Target Market(s)

The families who make the decision are 60-70 years old. They are not not "rich" but they have saved well and usually have more than 1 million in assets.

Industry/Entity Type

Senior Living, Memory Care

Font styles to use
Serif

Colors
00AB8E
00BBA5
67D7C9
C6EFE9
E9F9F6
FFC000
F8CF3A
FAE287
FDF2CF
FEFAEE

Requirements
Must have
• When compromise is not an option...
Nice to have
• A difficult balance of beautiful and activities (happy people), but also communicating that we handle difficult and complex care.

```html
<!DOCTYPE html>
<html lang="en">
<head>
<meta charset="utf-8">
<title>Bright Meadow Haven – Brochure</title>
<link rel="stylesheet" href="https://fonts.googleapis.com/css2?family=Playfair+Display:ital,wght@0,400;0,500;1,400&family=Arimo:wght@400;500;700&display=swap">
<style>
:root{
  --teal:#00AB8E;
  --teal-2:#00BBA5;
  --gold:#FFC000;
  --ink:#1a1a1a;
  --navy:#13342f;
  --stage:#f0eff0;
  --paper:#ffffff;
}
*{margin:0;padding:0;box-sizing:border-box}
html,body{width:1200px;height:593px;overflow:hidden;background:var(--stage)}
body{position:relative;font-family:"Arimo",Arial,sans-serif;color:var(--ink)}
h1,h2{font-weight:400}
.stage-band{position:absolute;left:0;top:0;width:251px;height:593px;background:var(--teal)}
.page{position:absolute;background:var(--paper);box-shadow:0 2px 8px rgba(0,0,0,.12);overflow:hidden}
.photo{position:absolute}

/* brand lockup */
.brand{position:absolute;text-align:center}
.brand-name{font-family:"Playfair Display",Georgia,serif;font-weight:500;color:var(--navy);white-space:nowrap}
.brand-sub{font-family:"Playfair Display",Georgia,serif;font-weight:400;color:var(--ink);white-space:nowrap}
.brand-rule{height:1px;background:var(--gold)}

/* cover */
.cover{left:46px;top:85px;width:320px;height:453px}
.cover h1{position:absolute;left:23px;top:69px;font-family:"Playfair Display",Georgia,serif;font-weight:400;font-size:21.5px;line-height:21px;color:var(--ink)}
.cover .lede{position:absolute;left:23px;top:121px;font-size:8.4px;line-height:12.2px}
.cover .promise{position:absolute;left:23px;top:154px;width:105px;font-family:"Playfair Display",Georgia,serif;font-size:8px;line-height:10.5px;color:var(--teal)}
.cover .block{position:absolute}
.cover .loc{position:absolute;left:203px;top:344px;font-size:7.7px;line-height:9.5px}
.cover .loc-rule{position:absolute;left:203px;top:367px;width:35px;height:1px;background:var(--ink)}
.cover .cta{position:absolute;left:203px;top:371px;font-size:7.9px;font-weight:700}
.cover .phone{position:absolute;left:203px;top:381px;font-size:7.9px}
.cover .web{position:absolute;left:203px;top:397px;font-size:6.8px;white-space:nowrap}

/* inside pages */
.inside{top:152px;width:226px;height:318px}
.accent-bar{position:absolute;width:2px;background:var(--teal)}
.h2{position:absolute;font-family:"Playfair Display",Georgia,serif;font-weight:400;font-size:9.6px;line-height:10.4px;color:var(--ink);white-space:nowrap}
.kicker{position:absolute;font-size:5.4px;line-height:6.6px}
.body{position:absolute;font-size:3.6px;line-height:5.65px;color:#222}
.footer{position:absolute;left:0;top:304px;width:100%;height:9px;background:var(--teal);color:#fff;font-size:4.2px;line-height:9px;text-align:center}
.side-band{position:absolute;left:171px;top:14px;width:55px;height:290px;background:var(--teal)}
.bullets{position:absolute;font-size:4.2px;line-height:9.2px;white-space:nowrap}
.bullets span{margin-right:4px}
.bullets span::before{content:"";display:inline-block;width:1.8px;height:1.8px;border-radius:50%;background:var(--teal);margin-right:2px;vertical-align:middle}
</style>
</head>
<body>
<div class="stage-band"></div>

<div class="brand" style="left:470px;top:58px;width:260px">
  <div class="brand-name" style="font-size:31px;line-height:36px">Bright Meadow Haven</div>
  <div class="brand-rule" style="margin:3px 6px 5px"></div>
  <div class="brand-sub" style="font-size:20px;line-height:22px">Residential Assisted Living</div>
</div>

<!-- Cover -->
<section class="page cover">
  <div class="brand" style="left:23px;top:30px;width:100px">
    <div class="brand-name" style="font-size:10.5px;line-height:12px">Bright Meadow Haven</div>
    <div class="brand-rule" style="margin:1px 2px 2px"></div>
    <div class="brand-sub" style="font-size:7.2px;line-height:9px">Residential Assisted Living</div>
  </div>
  <h1>The Perfect Balance of<br>Safety &amp; Warmth</h1>
  <p class="lede">Professional &amp; Friendly Care in a<br>Home Environment</p>
  <p class="promise">When compromise is not an option...</p>

  <div class="photo" role="img" aria-label="Portrait of the owner in a light shirt" style="left:135px;top:159px;width:58px;height:58px;background:linear-gradient(160deg,#e9e2d6,#c9b8a0)"></div>
  <div class="photo" role="img" aria-label="Residents sharing drinks under a patio umbrella in the garden" style="left:195px;top:117px;width:104px;height:100px;background:linear-gradient(180deg,#d9a98a 0%,#9aa86e 45%,#6f7a5a 100%)"></div>
  <div class="photo" role="img" aria-label="Residents in party masks celebrating at a dining table" style="left:98px;top:220px;width:94px;height:100px;background:linear-gradient(160deg,#8d7c6a,#c4aa92)"></div>
  <div class="photo" role="img" aria-label="Harpist performing for residents in the living room" style="left:195px;top:220px;width:104px;height:100px;background:linear-gradient(160deg,#e7e1d8,#9f9a8a 70%,#5f7c4a)"></div>
  <div class="block" style="left:39px;top:262px;width:56px;height:58px;background:var(--teal)"></div>
  <div class="photo" role="img" aria-label="Exterior of the single-storey residence with driveway" style="left:0;top:324px;width:95px;height:100px;background:linear-gradient(180deg,#dfe3e4 0%,#b9a98f 55%,#d8d6cf 100%)"></div>
  <div class="block" style="left:98px;top:324px;width:94px;height:100px;background:var(--gold)"></div>

  <p class="loc">Oakridge &amp; Willow Creek<br>Assisted Living</p>
  <div class="loc-rule"></div>
  <p class="cta">Give Us a Call Today</p>
  <p class="phone">555-014-2290</p>
  <p class="web">www.brightmeadowhaven.example</p>
</section>

<!-- Page 2 -->
<section class="page inside" style="left:404px">
  <div class="accent-bar" style="left:15px;top:14px;height:26px"></div>
  <h2 class="h2" style="left:21px;top:18px">Assisted Living in<br>Oakridge &amp; Willow Creek</h2>
  <p class="kicker" style="left:21px;top:45px">Quality of Life You Want for Your Loved Ones</p>
  <p class="body" style="left:21px;top:57px;width:118px">At Bright Meadow Haven Residential Assisted Living, our team of highly trained and caring professionals provides a welcoming and comfortable assisted living environment for our residents to enjoy for many years to come. Unlike other communities, our Oakridge assisted living home is located in a residential setting because we believe it brings a greater value to our residents as they maintain feelings of safety, warmth, and familiarity. The most beneficial factor of living in our community is the great amount of personal care and attention we are able to give each one of our residents. In fact, we maintain the highest caregiver to resident ratio in the assisted living industry. More than anything, we believe Bright Meadow Haven is the trusted solution for families who put quality care as their highest priority.</p>
  <div class="photo" role="img" aria-label="Long white covered porch with ceiling fans" style="left:146px;top:14px;width:80px;height:141px;background:linear-gradient(180deg,#f4f3ef,#d7d4cc 70%,#bdb9ae)"></div>

  <div class="accent-bar" style="left:15px;top:163px;height:25px"></div>
  <h2 class="h2" style="left:21px;top:166px">Learn More About Bright Meadow Haven<br>Residential Assisted Living</h2>
  <p class="kicker" style="left:21px;top:194px;width:92px">Our Oakridge &amp; Willow Creek Senior Caregivers are Compassionate and Attentive</p>
  <p class="kicker" style="left:118px;top:194px;width:90px">Exceptional Care, Safety, and Customer Service</p>
  <p class="body" style="left:21px;top:220px;width:92px">Though it may be obvious that Bright Meadow Haven takes care of older folks, what's not as evident is how we do it. We have had many people drive up and down our street and call us saying "I can't find your building, there's just a bunch of houses here." It's so common in our society that the elderly are mainly served in institutional, apartment-like buildings. We are used to it and chuckle as we explain that indeed, they are on the right street.</p>
  <p class="body" style="left:118px;top:220px;width:92px">Bright Meadow Haven was started by and is operated by me (Theo) and I couldn't do it without the help of my wife, Clara. We live locally in Oakridge with our three little children: Lily, Owen, and Nora. We believe that every person, young and old, is created equal and deserves dignity. We set out to build a business that reflects that. The care, comfort, and happiness of our residents and their families is our daily pursuit.</p>
  <div class="footer">www.brightmeadowhaven.example</div>
</section>

<!-- Page 3 -->
<section class="page inside" style="left:668px">
  <div class="side-band"></div>
  <div class="accent-bar" style="left:15px;top:14px;height:26px"></div>
  <h2 class="h2" style="left:21px;top:19px">About Us</h2>
  <p class="kicker" style="left:21px;top:33px">Around the Clock Quality Care for Your Loved One.</p>

  <h2 class="h2" style="left:21px;top:69px">What We Do</h2>
  <div class="photo" role="img" aria-label="Caregiver assisting a resident in a sunlit lounge" style="left:150px;top:61px;width:62px;height:56px;background:linear-gradient(160deg,#5a4632,#d6a24e 60%,#e8c98a)"></div>
  <p class="body" style="left:21px;top:82px;width:125px">In America, people aren't used to assistance. We love independence and freedom and don't plan on giving them up. At Bright Meadow Haven we get that. When a person comes through our doors and needs to transition to more assistance, we work very hard to make it painless and, dare we say, enjoyable! We come alongside strong independent people and offer gentle, patient, and friendly help.</p>

  <h2 class="h2" style="left:21px;top:145px">Why We Do What We Do</h2>
  <div class="photo" role="img" aria-label="Residents chatting at a garden table" style="left:150px;top:137px;width:62px;height:56px;background:linear-gradient(180deg,#9bb47a,#6f8a52 60%,#b49c82)"></div>
  <p class="body" style="left:21px;top:163px;width:125px">Being in assisted living such a long time, we saw the spectrum of care that exists out there. We saw a need for higher acuity care. So we set out to find the sweet balance of high quality care combined with a home atmosphere. We do that through a three-pronged method. First, we partner with licensed medical help every step of the way. Second, we hire CNAs, medical assistants, and nurses on their way to becoming registered. Third, we only choose homes that are spacious and inviting. We believe this balance accomplishes our pursuit of doing for our residents what we would like done for us.</p>

  <h2 class="h2" style="left:21px;top:229px">Why We're Residential</h2>
  <div class="photo" role="img" aria-label="Residents relaxing together in a bright living room" style="left:150px;top:220px;width:62px;height:56px;background:linear-gradient(160deg,#eeeae2,#b9a68e 65%,#7d6a55)"></div>
  <p class="body" style="left:21px;top:247px;width:125px">The residential assisted living model allows us to keep the caregiver to resident ratio small. Simply put, the more residents, the more the caregivers are spread thin. In our environment we can achieve what we believe is the ideal ratio. We are also able to get to know every resident very closely. This is great relationally, but it's also medically advantageous since we are able to quickly assess a change in medical condition.</p>
  <div class="footer">www.brightmeadowhaven.example</div>
</section>

<!-- Page 4 -->
<section class="page inside" style="left:932px">
  <div class="photo" role="img" aria-label="Residents visiting an ice cream truck outside the home" style="left:0;top:0;width:226px;height:77px;background:linear-gradient(90deg,#5f6e4a,#9aa7b0 45%,#e4e6ea 70%,#d9577a)"></div>
  <div class="accent-bar" style="left:16px;top:88px;height:25px"></div>
  <h2 class="h2" style="left:21px;top:92px">Our Services</h2>
  <p class="kicker" style="left:21px;top:106px">Around the Clock Quality Care for Your Loved One.</p>
  <div class="bullets" style="left:21px;top:120px">
    <span>Alzheimer's &amp; Dementia Care</span><span>Stroke Care</span><span>Parkinson's Care</span><br>
    <span>Limited Mobility</span><span>Hospice Care</span><span>Skin &amp; Incontinence Care</span><span>Short Term Stays</span>
  </div>
  <h2 class="h2" style="left:21px;top:147px">Oakridge Assisted Living Facility</h2>
  <p class="kicker" style="left:21px;top:162px">We'll Treat Your Loved One Like Family: 555.014.2290</p>
  <p class="body" style="left:21px;top:173px;width:190px">We at Bright Meadow Haven Residential Assisted Living realize that entrusting the health and well-being of your elderly loved one to an assisted living home is no easy decision. You want to find a home that will provide them with exceptional care in a beautiful and pleasant setting. Most assisted living homes look and feel institutional and sterile - but not ours. Our assisted living home looks like the other homes that line our residential street. We opened our doors with the purpose of providing the best combination of professional care and a comfortable home environment for seniors in Oakridge. If you are seeking assisted living in Willow Creek or Oakridge, you can feel confident turning to Bright Meadow Haven!</p>
  <p class="kicker" style="left:21px;top:226px">Providing High Quality Care Around The Clock</p>
  <p class="body" style="left:21px;top:237px;width:160px">The services we offer at our Oakridge assisted living home are backed by many years of experience in the care industry. Our exceptional safety, care, and customer service have benefited countless residents, not to mention their families. We emphasize the importance of family communication and do what we can to create a safe and welcoming environment that makes it easy and encourages family members to visit their loved ones.</p>
  <p class="body" style="left:21px;top:273px;width:186px">Thanks to our small chain of command, we can minimize errors, which is what often plagues larger assisted living homes. In the event your loved one needs hospice care, our home can also assist you with that transition, right under our own roof. We extend our services to families in Cedar Bay, Pine Hollow, Elm Ridge, Maple Flats, and Willow Creek.</p>
  <div class="footer">www.brightmeadowhaven.example</div>
</section>
</body>
</html>
```